Public Speaking Book for aspiring, ambitious speakers

I'm looking for a 6x9 book cover (Brevora standard) as well as ebook and audiobook formats.

I'm looking for orange font on a white background as these are my brand colours.

Feel free to use some yellow and gold too if you deem it appropriate.

Title: Climb and Kindle
Subtitle: Find Your Voice. Tell Your Story. Share your Message.
Author: Tobias Wenlock

I would like to have a picture of a female speaker on the front cover.

Alternatively, some kind of image that symbolises public speaking like a microphone, podium etc

Target Market(s)

Aspiring professional speakers

Colors
f78f20

Requirements
Must have
• Correct spelling!
Nice to have
• A logo or picture that fits the theme, but no pressure if you can't think of anything
Should not have
• No men in suits please. I don't want this to have a 1980s corporate look.

```html
<!DOCTYPE html>
<html lang="en">
<head>
<meta charset="utf-8">
<title>Climb and Kindle — Book Cover Wrap</title>
<link rel="stylesheet" href="https://fonts.googleapis.com/css2?family=Inter:wght@400;600;700;800&family=Inter+Tight:wght@400;600;700&display=swap">
<style>
  :root {
    --brand-orange: #e38b2c;
    --ink: #1a1a1a;
    --paper: #ffffff;
    --band-text: #ffffff;
  }
  * { margin: 0; padding: 0; box-sizing: border-box; }
  html, body {
    width: 1200px;
    height: 881px;
    overflow: hidden;
    background: var(--paper);
  }
  .cover-wrap {
    position: relative;
    width: 1200px;
    height: 881px;
    background: var(--paper);
    font-family: "Inter", "Helvetica Neue", Arial, sans-serif;
    color: var(--ink);
    overflow: hidden;
  }

  /* Back cover */
  .back-cover {
    position: absolute;
    left: 0; top: 0;
    width: 583px; height: 881px;
  }
  .back-headline {
    position: absolute;
    left: 60px; width: 474px; top: 74px;
    text-align: center;
    color: var(--brand-orange);
    font-family: "Inter Tight", "Helvetica Neue", Arial, sans-serif;
    font-weight: 600;
    font-size: 19px;
    line-height: 25px;
  }
  .back-blurb {
    position: absolute;
    left: 76px; top: 0;
    width: 460px; height: 881px;
    font-family: "Inter Tight", "Helvetica Neue", Arial, sans-serif;
    font-size: 15px;
    line-height: 21.5px;
    white-space: nowrap;
  }
  .back-blurb p { position: absolute; left: 0; }
  .back-blurb .para-1 { top: 145px; }
  .back-blurb .para-2 { top: 226px; }
  .back-blurb .para-3 { top: 287px; }
  .back-blurb .para-4 { top: 348px; }
  .back-blurb .para-5 { top: 407px; }
  .back-blurb .para-6 { top: 489px; }
  .back-closing {
    position: absolute;
    left: 76px; top: 532px;
    white-space: nowrap;
    color: var(--brand-orange);
    font-family: "Inter Tight", "Helvetica Neue", Arial, sans-serif;
    font-weight: 600;
    font-size: 18.5px;
    line-height: 26px;
  }
  .cable-photo {
    position: absolute;
    left: 0; top: 620px;
    width: 323px; height: 83px;
  }

  /* Spine */
  .spine {
    position: absolute;
    left: 583px; top: 0;
    width: 35px; height: 881px;
  }
  .spine-title, .spine-author {
    position: absolute;
    left: 50%;
    white-space: nowrap;
    font-weight: 700;
    writing-mode: vertical-rl;
    transform: translateX(-50%);
  }
  .spine-title {
    top: 187px;
    color: var(--brand-orange);
    font-size: 22px;
  }
  .spine-author {
    top: 452px;
    color: var(--ink);
    font-size: 19px;
  }

  /* Front cover */
  .front-cover {
    position: absolute;
    left: 618px; top: 0;
    width: 582px; height: 881px;
  }
  .front-title {
    position: absolute;
    left: 0; width: 582px; top: 62px;
    text-align: center;
    color: var(--brand-orange);
    font-weight: 700;
    font-size: 106px;
    line-height: 114px;
    letter-spacing: -2px;
  }
  .front-subtitle {
    position: absolute;
    left: 0; width: 582px; top: 304px;
    text-align: center;
    color: var(--ink);
    font-weight: 600;
    font-size: 33px;
    line-height: 39px;
    letter-spacing: -0.4px;
  }
  .microphone-photo {
    position: absolute;
    left: 136px; top: 488px;
    width: 354px; height: 287px;
  }

  /* Author band */
  .author-band {
    position: absolute;
    left: 0; top: 775px;
    width: 1200px; height: 106px;
    background: var(--brand-orange);
  }
  .band-author {
    position: absolute;
    left: 618px; width: 582px; top: 20px;
    text-align: center;
    color: var(--band-text);
    font-weight: 700;
    font-size: 54px;
    line-height: 64px;
    letter-spacing: -0.8px;
  }
</style>
</head>
<body>
<main class="cover-wrap">

  <section class="back-cover">
    <h2 class="back-headline">Have you always wanted to speak up but others<br>shut you down?</h2>
    <div class="back-blurb">
      <p class="para-1">Have you always felt that you had something to say, you just didn’t<br>know what it was? Have you always known you were meant to<br>make a difference in the world, you just didn’t know how?</p>
      <p class="para-2">It sounds like you are meant to be a speaker. And there has never<br>been a better time to start.</p>
      <p class="para-3">This book will teach you everything you need to know in order to<br>set the foundations for a successful speaking journey.</p>
      <p class="para-4">You are going to learn to develop confidence in your abilities, clarity<br>on your message, and connection with your future audiences.</p>
      <p class="para-5">It doesn’t matter where you are starting from. What matters is your<br>desire to impact people’s lives and your commitment to learning<br>what is necessary to make that happen.</p>
      <p class="para-6">The speaker’s journey is open to anyone.</p>
    </div>
    <p class="back-closing">The question is: are you ready to take that first step?</p>
    <svg class="cable-photo" role="img" aria-label="Photo of an orange microphone cable ending in a connector plug" viewBox="0 0 323 83" preserveAspectRatio="none">
      <defs>
        <linearGradient id="cableTone" x1="0" y1="1" x2="1" y2="0">
          <stop offset="0" stop-color="#f3c89a"/>
          <stop offset="0.7" stop-color="#f8e2c9"/>
          <stop offset="1" stop-color="#ffffff"/>
        </linearGradient>
      </defs>
      <rect width="323" height="83" fill="url(#cableTone)"/>
    </svg>
  </section>

  <section class="spine">
    <span class="spine-title">Climb and Kindle</span>
    <span class="spine-author">Tobias Wenlock</span>
  </section>

  <section class="front-cover">
    <h1 class="front-title">Climb and<br>Kindle</h1>
    <p class="front-subtitle">Find your voice,<br>tell your story and<br>share your message<br>as a speaker</p>
    <svg class="microphone-photo" role="img" aria-label="Photo of a raised hand gripping a handheld microphone with an orange cable" viewBox="0 0 354 287" preserveAspectRatio="none">
      <defs>
        <linearGradient id="micTone" x1="0" y1="0" x2="1" y2="1">
          <stop offset="0" stop-color="#d9d9d9"/>
          <stop offset="0.45" stop-color="#f2cfb0"/>
          <stop offset="1" stop-color="#f0a95c"/>
        </linearGradient>
      </defs>
      <rect width="354" height="287" fill="url(#micTone)"/>
    </svg>
  </section>

  <footer class="author-band">
    <p class="band-author">Tobias Wenlock</p>
  </footer>

</main>
</body>
</html>
```